OILFIELD SERVICE COMPANY NEEDS A UPDATED BUSINESS CARD

Brackwell Drill Supply, Inc. is an oilfield service company headquartered in Broussard, LA with additional locations in Ruston, LA ; Palestine, TX ; Carthage, TX ; and San Angelo, TX. Our primary service lines are Fishing, Casing Cutting, Section Milling, Whipstocks, Rentals. We are looking for a modern, eye catching business card that highlights our services and locations. We have the motto "No Problems . . . Only Solutions" We would like to see clean, modern designs.

Industry/Entity Type

Business

Contact Information for Business Card

Information must include phone, fax (dependent on which location you work at), cell and email. I would like all the locations to be listed on the back with phone numbers.

Broussard, LA : 337.412.6093
Ruston, LA : 318.730.4162
Carthage, TX : 903.217.5836
Palestine, TX : 903.861.4075
San Angelo, TX : 325.309.7481

Requirements
Must have
• Services on front of card : Fishing, Casing Cutting, Section Milling, Whipstocks, Rentals
• www.brackwelldrillsupply.example
Nice to have
• I like the look of watermark images or background logos.

```html
<!DOCTYPE html>
<html lang="en">
<head>
<meta charset="utf-8">
<title>Brackwell Drill Supply — Business Card</title>
<link rel="stylesheet" href="https://fonts.googleapis.com/css2?family=Oswald:wght@500;600&family=Roboto:wght@400;500;700&display=swap">
<style>
  :root {
    --bg: #e9e6e1;
    --white: #ffffff;
    --red: #e31e25;
    --black: #262324;
    --ink: #231f20;
    --text-light: #ffffff;
    --text-muted: #d6d6d6;
    --text-grey: #6b6768;
  }
  * { box-sizing: border-box; margin: 0; padding: 0; }
  html, body {
    width: 1200px; height: 1018px; overflow: hidden;
    background: var(--bg);
    font-family: "Roboto", Arial, sans-serif;
  }
  .sheet { position: relative; width: 1200px; height: 1018px; }
  .card {
    position: absolute; left: 230px; width: 740px; height: 420px;
    overflow: hidden;
    box-shadow: 0 10px 28px rgba(0,0,0,0.22);
  }
  .card--front { top: 54px; background: var(--white); }
  .card--back { top: 544px; background: var(--black); }

  /* Front */
  .front-brand {
    position: absolute; left: 0; top: 0; width: 100%; height: 190px;
    background: var(--white);
    padding: 0 46px;
  }
  .brand {
    position: absolute; left: 46px; top: 110px;
    display: flex; align-items: center; gap: 14px;
  }
  .brand__mark { width: 44px; height: 44px; background: var(--red); }
  .brand__name {
    font-weight: 700; font-size: 22px; color: var(--red);
    letter-spacing: 0.5px;
  }
  .services {
    position: absolute; right: 46px; top: 40px;
    list-style: none; text-align: right;
    font-family: "Oswald", Arial, sans-serif; font-weight: 500;
    font-size: 14px; letter-spacing: 1.5px; text-transform: uppercase;
    color: var(--ink); line-height: 1.75;
  }
  .services li::after {
    content: ""; display: inline-block; width: 6px; height: 6px;
    background: var(--red); margin-left: 10px; vertical-align: middle;
  }

  .front-contact {
    position: absolute; left: 0; top: 190px; width: 100%; height: 84px;
    background: var(--red);
    display: flex; justify-content: space-between; align-items: center;
    padding: 0 46px;
    color: var(--text-light); font-size: 15px;
  }
  .contact-list { list-style: none; display: flex; flex-direction: column; gap: 10px; }
  .contact-list li { display: flex; align-items: center; gap: 10px; }
  .contact-list svg { width: 14px; height: 14px; fill: var(--text-light); flex: none; }

  .front-identity {
    position: absolute; left: 0; top: 274px; width: 100%; height: 146px;
    background: var(--black);
    display: flex; justify-content: space-between; align-items: center;
    padding: 0 46px;
    color: var(--text-light);
  }
  .person__name {
    font-family: "Oswald", Arial, sans-serif; font-weight: 600;
    font-size: 30px; letter-spacing: 1px; text-transform: uppercase;
  }
  .person__title {
    font-size: 15px; letter-spacing: 1.5px; text-transform: uppercase;
    color: var(--text-muted); margin-top: 2px;
  }
  .address {
    font-style: normal; font-size: 16px; line-height: 1.55;
    text-align: right; letter-spacing: 0.5px;
  }

  /* Back */
  .back-bands { position: absolute; inset: 0; width: 100%; height: 100%; }
  .locations {
    position: absolute; left: 210px; top: 56px; width: 330px;
    color: var(--text-light);
  }
  .locations__title {
    font-family: "Oswald", Arial, sans-serif; font-weight: 600;
    font-size: 20px; letter-spacing: 2px; text-transform: uppercase;
    padding-bottom: 10px; margin-bottom: 12px;
    border-bottom: 2px solid var(--red);
  }
  .locations__list { list-style: none; }
  .locations__list li {
    display: flex; justify-content: space-between;
    font-size: 16px; line-height: 1.9; letter-spacing: 0.5px;
  }
  .locations__city { color: var(--text-light); }
  .locations__phone { color: var(--text-muted); }
</style>
</head>
<body>
<main class="sheet">

  <section class="card card--front" aria-label="Business card front">
    <div class="front-brand">
      <ul class="services">
        <li>Fishing</li>
        <li>Casing Cutting</li>
        <li>Section Milling</li>
        <li>Whipstocks · Rentals</li>
      </ul>
      <div class="brand">
        <span class="brand__mark"></span>
        <span class="brand__name">Brackwell Drill Supply, Inc.</span>
      </div>
    </div>

    <div class="front-contact">
      <ul class="contact-list">
        <li>
          <svg viewBox="0 0 24 24" aria-hidden="true"><path d="M6.6 10.8a15.1 15.1 0 0 0 6.6 6.6l2.2-2.2a1 1 0 0 1 1-.25 11.4 11.4 0 0 0 3.6.57 1 1 0 0 1 1 1V20a1 1 0 0 1-1 1A17 17 0 0 1 3 4a1 1 0 0 1 1-1h3.5a1 1 0 0 1 1 1c0 1.25.2 2.45.57 3.6a1 1 0 0 1-.25 1z"/></svg>
          <span>337.412.6093</span>
        </li>
        <li>
          <svg viewBox="0 0 24 24" aria-hidden="true"><path d="M7 1h10a2 2 0 0 1 2 2v18a2 2 0 0 1-2 2H7a2 2 0 0 1-2-2V3a2 2 0 0 1 2-2zm0 4v13h10V5zm5 14.5a1 1 0 1 0 0 2 1 1 0 0 0 0-2z"/></svg>
          <span>337.412.6093</span>
        </li>
      </ul>
      <ul class="contact-list">
        <li>
          <svg viewBox="0 0 24 24" aria-hidden="true"><path d="M2 5h20v14H2zm2 2v.5l8 5 8-5V7z"/></svg>
          <span>dale@brackwelldrill.example</span>
        </li>
        <li>
          <svg viewBox="0 0 24 24" aria-hidden="true"><circle cx="12" cy="12" r="9" fill="none" stroke="#fff" stroke-width="2"/><path d="M3 12h18M12 3c3 3 3 15 0 18M12 3c-3 3-3 15 0 18" fill="none" stroke="#fff" stroke-width="1.6"/></svg>
          <span>www.brackwelldrillsupply.example</span>
        </li>
      </ul>
    </div>

    <div class="front-identity">
      <div class="person">
        <p class="person__name">Dale Thibodeaux</p>
        <p class="person__title">General Manager</p>
      </div>
      <address class="address">412 Verot Mill Road,<br>Suite 3, Broussard</address>
    </div>
  </section>

  <section class="card card--back" aria-label="Business card back">
    <svg class="back-bands" viewBox="0 0 740 420" preserveAspectRatio="none" aria-hidden="true">
      <polygon points="0,0 170,0 0,150" fill="#e31e25"/>
      <polygon points="430,420 560,250 740,250 740,420" fill="#e31e25"/>
    </svg>
    <div class="locations">
      <h2 class="locations__title">Locations</h2>
      <ul class="locations__list">
        <li><span class="locations__city">Broussard, LA</span><span class="locations__phone">337.412.6093</span></li>
        <li><span class="locations__city">Ruston, LA</span><span class="locations__phone">318.730.4162</span></li>
        <li><span class="locations__city">Carthage, TX</span><span class="locations__phone">903.217.5836</span></li>
        <li><span class="locations__city">Palestine, TX</span><span class="locations__phone">903.861.4075</span></li>
        <li><span class="locations__city">San Angelo, TX</span><span class="locations__phone">325.309.7481</span></li>
      </ul>
    </div>
  </section>

</main>
</body>
</html>
```